Pamphlet design, flyer, and poster for cardiology office

Hello design experts out there. We are looking for the following:
1. Brochure : accordian Z fold design.
2. Company folder with content (see pamphlet idea and design example.
3. Large pull up poster/banner.

They are used promote our Cardiology office.

The services our office provide are labelled 1-6 below.

A. For the company folder, please create a front and back insert x 3 that is staggered (see pamphlet idea, sunday; and small-medium-large, Monday) and inserted on the right side. Our referral form that has been designed and will be included on the left (referral BCC Monday). Feel free to use the same themes.
Inserts in folder:
• 1. Echocardiogram and 2. Stress Echocardiogram (largest page front and back)
• 3. Holter/Loop monitor and 4. Ambulatory blood pressure monitoring (medium sized page front and back)
• 5. Electrocardiogram and 6. Cardiac Consultations (smallest page front and back)

In terms of content for the folder inserts, our word content will likely not be more than 2 or 3 sentences (we are drafting them now). Please ensure colorful and attractive graphics are used to highlight these tests. Please use, where possible, pictures of tests more than of people. The goal is to emphasize the role of the office as a testing center. Feel free to look them up online (eg. Echo, stress echo, Holter monitoring etc).

B. For the accordian Z fold brochure, please design it such where by each item we offer (from 1-6 below) occupy 1 page of fold, with the exception where item 5 - 6 combined into 1 page. The front page of course will be the office logo and address etc.

C. For the Large pull up poster display for BRAMLEY CARDIAC CENTRE - simple, with picture. Dimensions 33" x 81"
This banner will have our logo, and a summary of ll the services we provide (1 - 6)

Items need to be graphics heavy and attractive as we are trying to avoid making it wordy.

Target Market(s)

Referring physicians, patietns

Industry/Entity Type

Health Care

Requirements
Must have
• Attractive graphics and pictures.
• Most graphics emphasize diagnostic testing we do.
Should not have
• Too much word content

```html
<!DOCTYPE html>
<html lang="en">
<head>
<meta charset="utf-8">
<title>Bramley Cardiac Centre – Presentation Folder</title>
<link rel="stylesheet" href="https://fonts.googleapis.com/css2?family=Cinzel:wght@500;600&family=Libre+Baskerville&family=Lato:wght@400&display=swap">
<style>
  :root{
    --navy:#262766;
    --red:#9b1119;
    --ink:#1c1c1c;
    --paper:#ffffff;
  }
  *{margin:0;padding:0;box-sizing:border-box}
  html,body{width:1200px;height:1200px;overflow:hidden;background:var(--paper)}
  .folder{position:relative;width:1200px;height:1200px}
  .folder-art{position:absolute;inset:0;width:1200px;height:1200px}
  .brand-name{position:absolute;font-family:"Cinzel",serif;font-weight:600;color:var(--navy);text-align:center;line-height:1}
  .brand-name .line-main{display:block;font-size:18px;letter-spacing:.3px}
  .brand-name .line-sub{display:block;font-size:12px;margin-top:2px;letter-spacing:.8px}
  .brand-name--back{left:77px;top:596px;width:200px}
  .brand-name--front{left:616px;top:182px;width:220px}
  .brand-name--front .line-main{font-size:19px}
  .brand-name--pocket{left:172px;top:884px;width:260px;color:var(--paper);transform:rotate(180deg)}
  .brand-name--pocket .line-main{font-size:24px}
  .brand-name--pocket .line-sub{font-size:17px}
  .contact-list{position:absolute;left:98px;top:657px;list-style:none;font-family:"Lato",sans-serif;font-size:15px;color:var(--ink);line-height:19px}
  .contact-list li{display:flex;align-items:flex-start;gap:5px;margin-bottom:11px}
  .contact-list svg{flex:none;width:13px;height:13px;margin-top:3px;fill:var(--red)}
  .headline{position:absolute;left:622px;top:602px}
  .headline .kicker{font-family:"Cinzel",serif;font-weight:600;font-size:24px;color:var(--red);letter-spacing:.3px;line-height:1}
  .headline .lede{font-family:"Libre Baskerville",serif;font-size:31px;color:var(--ink);line-height:1.2;margin-top:2px}
  .web-address{position:absolute;left:594px;width:524px;top:783px;text-align:center;font-family:"Lato",sans-serif;font-size:13px;letter-spacing:4px;color:var(--paper)}
</style>
</head>
<body>
<main class="folder">
  <svg class="folder-art" viewBox="0 0 1200 1200" xmlns="http://www.w3.org/2000/svg">
    <defs>
      <linearGradient id="navyPhoto" x1="0" y1="0" x2="1" y2="1">
        <stop offset="0" stop-color="#2a2b70"/>
        <stop offset=".5" stop-color="#34368a"/>
        <stop offset="1" stop-color="#2a2b70"/>
      </linearGradient>
      <linearGradient id="consolePhoto" x1="0" y1="0" x2="1" y2="1">
        <stop offset="0" stop-color="#f1ebdf"/>
        <stop offset=".35" stop-color="#e6e1d6"/>
        <stop offset=".65" stop-color="#c9ccd4"/>
        <stop offset="1" stop-color="#e9eaed"/>
      </linearGradient>
      <linearGradient id="mistBg" x1="0" y1="0" x2="1" y2="0">
        <stop offset="0" stop-color="#f4f5f6"/>
        <stop offset=".5" stop-color="#ebedef"/>
        <stop offset="1" stop-color="#f2f3f4"/>
      </linearGradient>
      <linearGradient id="heartProp" x1="0" y1="1" x2="1" y2="0">
        <stop offset="0" stop-color="#d3d6db"/>
        <stop offset=".55" stop-color="#e7c9cb"/>
        <stop offset="1" stop-color="#d8363c"/>
      </linearGradient>
      <linearGradient id="pocketRight" x1="0" y1="0" x2="1" y2="1">
        <stop offset="0" stop-color="#8f121a"/>
        <stop offset=".5" stop-color="#9c1a22"/>
        <stop offset="1" stop-color="#8a0e16"/>
      </linearGradient>
    </defs>

    <!-- back cover -->
    <g class="back-cover">
      <rect x="70" y="114" width="524" height="702" fill="var(--paper)"/>
      <path d="M70 114 H594 V664 C420 618 200 520 70 368 Z" fill="url(#navyPhoto)" role="img" aria-label="Navy-tinted photo of a fingertip pulse oximeter and blood pressure monitor"/>
      <path d="M70 368 C200 520 420 618 594 664 V684 C420 642 200 540 70 378 Z" fill="var(--red)"/>
      <rect class="heart-stethoscope" x="336" y="690" width="226" height="112" rx="14" fill="url(#heartProp)" role="img" aria-label="Photo of a glossy red heart wrapped in a stethoscope"/>
    </g>

    <!-- front cover -->
    <g class="front-cover">
      <rect x="594" y="114" width="524" height="702" fill="url(#mistBg)"/>
      <g class="heart-window">
        <path d="M952 258 C920 206 830 206 760 246 C690 286 664 366 684 430 C716 532 880 610 1118 652" fill="none" stroke="var(--navy)" stroke-width="5"/>
        <path d="M952 258 C972 196 1010 146 1078 116" fill="none" stroke="var(--navy)" stroke-width="4"/>
        <path d="M964 248 C930 200 830 200 760 240 C690 280 670 360 690 420 C722 520 880 600 1118 640 V114 H1090 C1020 140 975 190 964 248 Z" fill="url(#consolePhoto)" stroke="var(--red)" stroke-width="8" role="img" aria-label="Photo of a stethoscope resting on an ultrasound console"/>
      </g>
      <path d="M594 664 C780 716 960 744 1118 744 V816 H594 Z" fill="var(--navy)"/>
      <path d="M594 664 C780 712 960 740 1118 740 V762 C960 764 780 734 594 684 Z" fill="var(--red)"/>
    </g>

    <!-- pockets -->
    <path class="pocket pocket--left" d="M70 816 H592 L572 1030 Q570 1048 552 1048 H70 L41 1024 V844 Z" fill="var(--red)"/>
    <path class="pocket pocket--right" d="M596 816 H1118 L1150 842 V1022 L1118 1048 H640 Q622 1048 620 1030 Z" fill="url(#pocketRight)" role="img" aria-label="Faint tinted photo of a heart monitor display"/>
  </svg>

  <div class="brand-name brand-name--back"><span class="line-main">BRAMLEY CARDIAC</span><span class="line-sub">CENTRE</span></div>

  <ul class="contact-list">
    <li><svg viewBox="0 0 12 12"><path d="M6 0a4 4 0 0 0-4 4c0 3 4 8 4 8s4-5 4-8a4 4 0 0 0-4-4zm0 5.6A1.6 1.6 0 1 1 6 2.4a1.6 1.6 0 0 1 0 3.2z"/></svg><span>118 Larkfield Road, Suite 3<br>Bramley ON K2R 4L7</span></li>
    <li><svg viewBox="0 0 12 12"><path d="M2.5 0.5l2 2.5-1.2 1.3c.8 1.6 2 2.8 3.4 3.6l1.3-1.2 2.5 2-1.4 2.3C5 10.5 1.5 7 .5 2z"/></svg><span>555-014-2290</span></li>
    <li><svg viewBox="0 0 12 12"><path d="M3 1h6v3H3zM1 5h10v5H9V8H3v2H1zM3 9h6v3H3z"/></svg><span>555-014-7815</span></li>
    <li><svg viewBox="0 0 12 12"><path d="M1 2h10v8H1zM1.5 2.5 6 6.5l4.5-4"/></svg><span>hello@bramleycardiac.org</span></li>
  </ul>

  <div class="brand-name brand-name--front"><span class="line-main">BRAMLEY CARDIAC</span><span class="line-sub">CENTRE</span></div>

  <div class="headline">
    <p class="kicker">LOREM IPSUM IS</p>
    <p class="lede">simply dummy text</p>
  </div>

  <p class="web-address">www.bramleycardiac.org</p>

  <div class="brand-name brand-name--pocket"><span class="line-main">BRAMLEY CARDIAC</span><span class="line-sub">CENTRE</span></div>
</main>
</body>
</html>
```